Tallyleaf Web Design

Create Website Design for Tallyleaf. Tallyleaf is online application for collaboration team work system (task list management). More concept design for this project please find attach file ("tallyleaf website concept.pdf") . But my concept is just describe minimal features not bind design

For tallyleaf logo, i had already attach files. But i had not decided what color i chose, so it's okay if you suggest logo color for your suitable website design.
Updates

Dear All Designer,

I like brisk carousel (http://quorvanlabs.example/brisk-carousel/),
may be your concept design can adjust with this concept.
but don't worry about script for brisk carousel, my team will be handle
You just make website design to suitable with brisk carousel

but if you had own website design concept are welcome

thanks

Target Market(s)

Business Company

Industry/Entity Type

Management

```html
<!DOCTYPE html>
<html lang="en">
<head>
<meta charset="utf-8">
<title>Tallyleaf — Customize Online Collaboration Team Work</title>
<link rel="stylesheet" href="https://fonts.googleapis.com/css2?family=Arimo:wght@400;700&display=swap">
<style>
  :root {
    --cream: #efe8de;
    --teal-nav: #327a6a;
    --ink-teal: #1e4e55;
    --brand-blue: #176a96;
    --btn-blue: #176e9c;
    --btn-orange: #e0703f;
    --accent-orange: #e8764a;
    --accent-purple: #a0609d;
    --accent-sage: #9dc7a0;
    --accent-teal: #4f9e8e;
    --green-light: #2f6f60;
    --green-dark: #1b4a40;
    --panel: #173a33;
    --peach: #eebf9f;
    --rule: #3b8273;
    --footnote: #4aa68e;
    --white: #ffffff;
  }
  * { box-sizing: border-box; margin: 0; padding: 0; }
  html, body { width: 1200px; height: 1000px; overflow: hidden; }
  body {
    font-family: "Arimo", Helvetica, Arial, sans-serif;
    background: radial-gradient(ellipse 70% 60% at 50% 45%, var(--green-light), var(--green-dark));
    position: relative;
  }

  .site-header { position: absolute; top: 0; left: 0; width: 1200px; height: 76px; background: var(--cream); }
  .brand { position: absolute; left: 203px; top: 14px; display: flex; align-items: center; gap: 10px; }
  .brand-name { font-size: 48px; font-weight: 700; color: var(--accent-teal); letter-spacing: -1px; line-height: 1; }
  .brand-dot { width: 16px; height: 16px; border-radius: 50%; background: var(--accent-purple); }
  .tagline { position: absolute; left: 455px; top: 44px; font-size: 14px; font-weight: 700; color: var(--ink-teal); }
  .auth { position: absolute; top: 18px; right: 202px; display: flex; gap: 10px; }
  .auth a { display: block; width: 76px; height: 42px; line-height: 40px; text-align: center; color: var(--white);
            font-weight: 700; font-size: 14px; text-decoration: none; border-radius: 3px;
            box-shadow: inset 0 -3px 0 rgba(0,0,0,.25); }
  .btn-login { background: var(--btn-orange); }
  .btn-signup { background: var(--btn-blue); }

  .main-nav { position: absolute; top: 76px; left: 0; width: 1200px; height: 41px; background: var(--teal-nav); }
  .main-nav ul { list-style: none; display: flex; justify-content: flex-end; gap: 32px; padding-right: 211px; }
  .main-nav a { display: block; line-height: 41px; color: var(--white); font-weight: 700; font-size: 14px; text-decoration: none; }

  .color-strip { position: absolute; top: 117px; left: 0; width: 1200px; height: 5px; display: flex; }
  .color-strip span { height: 5px; }

  .hero { position: absolute; top: 122px; left: 0; width: 1200px; height: 301px; background: var(--cream);
          box-shadow: 0 2px 4px rgba(0,0,0,.25); }
  .hero-arrow { position: absolute; top: 121px; }
  .hero-arrow.prev { left: 58px; }
  .hero-arrow.next { left: 1113px; }
  .hero-art { position: absolute; left: 195px; top: 28px; width: 300px; height: 228px; border-radius: 12px;
              background: radial-gradient(circle at 50% 45%, #c9dbe4, #e6dccf 70%); }
  .hero-title { position: absolute; left: 615px; top: 38px; font-size: 44px; line-height: 50px; font-weight: 700;
                color: var(--brand-blue); letter-spacing: -0.3px; }
  .hero-cta { position: absolute; left: 615px; top: 196px; width: 286px; height: 56px; background: var(--btn-blue);
              color: var(--white); font-size: 26px; font-weight: 700; text-align: center; line-height: 52px;
              border-radius: 3px; text-decoration: none; box-shadow: inset 0 -4px 0 rgba(0,0,0,.25); }

  .features { position: absolute; top: 423px; left: 200px; width: 800px; }
  .features-title { margin-top: 22px; font-size: 36px; font-weight: 700; color: var(--accent-orange);
                    text-shadow: 0 2px 2px rgba(0,0,0,.3); letter-spacing: .2px; }
  .rule { height: 1px; background: var(--rule); }
  .rule.top { margin-top: 15px; }
  .feature-list { position: relative; height: 233px; }
  .feature { position: absolute; top: 21px; }
  .feature-label { height: 42px; background: var(--panel); color: var(--peach); font-size: 16px; font-weight: 700;
                   text-align: center; line-height: 42px; }
  .feature-icon { margin-top: 13px; height: 134px; background: var(--panel); display: flex; align-items: center; justify-content: center;
                  border-bottom: 1px solid var(--rule); }
  .icon-fill { width: 130px; height: 96px; border-radius: 8px;
               background: radial-gradient(ellipse at 50% 50%, rgba(238,191,159,.35), rgba(238,191,159,0) 72%); }
  .feature.custom { left: 1px; width: 237px; }
  .feature.custom .feature-label { clip-path: polygon(0 0, 100% 0, 100% 100%, 0 100%, 4% 50%); }
  .feature.sync { left: 277px; width: 247px; }
  .feature.report { left: 563px; width: 237px; }
  .feature.report .feature-label { clip-path: polygon(0 0, 100% 0, 96% 50%, 100% 100%, 0 100%); }
  .footnote { margin-top: 22px; text-align: center; font-size: 11px; color: var(--footnote); }
</style>
</head>
<body>
  <header class="site-header">
    <div class="brand"><span class="brand-name">tallyleaf</span><span class="brand-dot"></span></div>
    <p class="tagline">Customize Online Collaboration Team Work</p>
    <div class="auth">
      <a class="btn-login" href="#">Login</a>
      <a class="btn-signup" href="#">Signup</a>
    </div>
  </header>

  <nav class="main-nav">
    <ul>
      <li><a href="#">Products</a></li>
      <li><a href="#">Solutions</a></li>
      <li><a href="#">Plans &amp; Pricing</a></li>
      <li><a href="#">Help/Support</a></li>
      <li><a href="#">Contact us</a></li>
    </ul>
  </nav>

  <div class="color-strip">
    <span style="width:110px;background:var(--accent-orange)"></span>
    <span style="width:202px;background:var(--accent-purple)"></span>
    <span style="width:199px;background:var(--accent-sage)"></span>
    <span style="width:200px;background:var(--accent-teal)"></span>
    <span style="width:180px;background:var(--btn-blue)"></span>
    <span style="width:192px;background:var(--accent-orange)"></span>
    <span style="width:117px;background:var(--accent-purple)"></span>
  </div>

  <section class="hero">
    <svg class="hero-arrow prev" width="28" height="40" viewBox="0 0 28 40"><path d="M24 2 L6 20 L24 38" fill="none" stroke="var(--brand-blue)" stroke-width="8"/></svg>
    <div class="hero-art" role="img" aria-label="Illustration of two team members sharing work through a cloud"></div>
    <h1 class="hero-title">Customize Online<br>Collaboration<br>Team Work</h1>
    <a class="hero-cta" href="#">Learn More</a>
    <svg class="hero-arrow next" width="28" height="40" viewBox="0 0 28 40"><path d="M4 2 L22 20 L4 38" fill="none" stroke="var(--brand-blue)" stroke-width="8"/></svg>
  </section>

  <main class="features">
    <h2 class="features-title">The Greatness or Differences from Tallyleaf</h2>
    <div class="rule top"></div>
    <div class="feature-list">
      <div class="feature custom">
        <div class="feature-label">Customize Application</div>
        <div class="feature-icon">
          <div class="icon-fill" role="img" aria-label="Line illustration of a personal folder"></div>
        </div>
      </div>
      <div class="feature sync">
        <div class="feature-label">Synchronize All Device</div>
        <div class="feature-icon">
          <div class="icon-fill" role="img" aria-label="Line illustration of a laptop and phone synced through a cloud"></div>
        </div>
      </div>
      <div class="feature report">
        <div class="feature-label">Report</div>
        <div class="feature-icon">
          <div class="icon-fill" role="img" aria-label="Line illustration of report pages"></div>
        </div>
      </div>
    </div>
    <div class="rule"></div>
    <p class="footnote">© 2013 Tallyleaf Trademarks belong to their respective owners. All rights reserved.</p>
  </main>
</body>
</html>
```